Flyer Design Project

Need a DL Size flyer (2 sided) for letter box marketing for our website www.brightwardsecure.com.au

Project Deadline Extended
Reason: Thank you for submitting the designs. We like few of the designs and will request those designers to changes few things to make it more suitable for us. Because of holidays need to extend the deadlines. Thank you.

Industry/Entity Type

Marketing

```html
<!DOCTYPE html>
<html lang="en">
<head>
<meta charset="utf-8">
<title>Brightward Secure – DL Flyer</title>
<link href="https://fonts.googleapis.com/css2?family=Arimo:wght@400;700&display=swap" rel="stylesheet">
<style>
  :root {
    --stage: #e9ecef;
    --blue-deep: #0a3f78;
    --blue-mid: #0d5fa8;
    --blue-bright: #1a86cf;
    --yellow: #f6c926;
    --white: #ffffff;
    --ink-soft: #dbe9f6;
    --green: #8cc63f;
    --green-dark: #4f8a12;
    --frame: #2a9ee8;
  }
  * { box-sizing: border-box; margin: 0; padding: 0; }
  html, body { width: 1200px; height: 749px; overflow: hidden; }
  body {
    background: var(--stage);
    font-family: "Arimo", Arial, sans-serif;
    position: relative;
  }
  .flyer {
    position: absolute;
    width: 619px;
    height: 295px;
    background: radial-gradient(ellipse at 45% 40%, var(--blue-bright) 0%, var(--blue-mid) 45%, var(--blue-deep) 100%);
    color: var(--white);
    overflow: hidden;
    box-shadow: 0 4px 14px rgba(0,0,0,.25);
  }
  .flyer--front { left: 86px; top: 65px; }
  .flyer--back { left: 497px; top: 390px; }

  /* Front */
  .camera-photo {
    position: absolute; left: 18px; top: 20px; width: 92px; height: 62px;
    background: linear-gradient(160deg, #f2f4f6, #9aa4ad);
    border-radius: 6px;
  }
  .brand-name {
    position: absolute; left: 115px; top: 30px;
    font-size: 27px; font-weight: 700; color: var(--yellow); white-space: nowrap;
  }
  .brand-tagline {
    position: absolute; left: 117px; top: 67px;
    font-size: 18px; font-weight: 700; white-space: nowrap;
  }
  .front-url {
    position: absolute; right: 22px; top: 12px;
    font-size: 10.5px; font-weight: 700;
  }
  .intro {
    position: absolute; left: 30px; top: 114px; width: 312px;
    font-size: 7.8px; line-height: 10px; color: var(--ink-soft); text-align: justify;
  }
  .intro p { margin-bottom: 8px; }
  .intro p.tight { margin-top: -8px; }
  .services {
    position: absolute; left: 30px; top: 229px;
    font-size: 7.8px; line-height: 9.4px;
  }
  .services h3 { font-size: 7.8px; font-weight: 700; }
  .services ul { list-style: none; color: var(--ink-soft); }
  .services li::before { content: "\2666\00a0"; }
  .devices-photo {
    position: absolute; left: 368px; top: 40px; width: 232px; height: 240px;
    background: linear-gradient(170deg, #6f8fa7 0%, #3a4a58 45%, #1f262d 100%);
    border-radius: 10px;
  }

  /* Back */
  .package {
    position: absolute; top: 26px; width: 160px;
  }
  .package--1 { left: 33px; }
  .package--2 { left: 236px; }
  .package--3 { left: 438px; }
  .package-photo {
    width: 152px; height: 91px;
    background: linear-gradient(180deg, #ffffff, #dfe4e8);
    border: 3px solid var(--frame);
    border-radius: 7px;
  }
  .package-title {
    margin-top: 14px; font-size: 13.5px; font-weight: 700; white-space: nowrap;
  }
  .package-sub { font-size: 5.8px; font-weight: 700; margin-top: 1px; white-space: nowrap; }
  .package-list {
    list-style: none; margin-top: 5px;
    font-size: 5.8px; line-height: 8.2px; color: var(--ink-soft);
  }
  .package-list li::before { content: "\2666\00a0"; }
  .price {
    display: inline-block; margin-top: 6px; margin-left: 5px;
    padding: 3px 7px; border-radius: 9px;
    background: var(--green); border: 1px solid var(--green-dark);
    font-size: 12px; font-weight: 700; color: var(--white);
  }
  .back-contact {
    position: absolute; left: 0; right: 0; top: 255px; text-align: center;
    font-size: 7.8px; color: var(--ink-soft);
  }
  .back-contact b { color: var(--white); }
  .back-url {
    position: absolute; left: 0; right: 0; top: 268px; text-align: center;
    font-size: 10px; font-weight: 700;
  }
</style>
</head>
<body>

<section class="flyer flyer--front" aria-label="Flyer front">
  <div class="camera-photo" role="img" aria-label="Photo of a white security camera on a wall mount"></div>
  <div class="brand-name">Brightward Secure</div>
  <div class="brand-tagline">CCTV System Specialist</div>
  <div class="front-url">www.brightwardsecure.com.au</div>

  <div class="intro">
    <p>We are a Sydney based company, providing high quality and affordable CCTV security system for home &amp; business clients since 2009. We have extensive experience and knowledge in the design, installation, maintenance and repair of wide range of CCTV systems.</p>
    <p>We can provide a wide range of home and business solutions – from a single camera system, to complex matrix video surveillance systems with multiple cameras, in multiple locations with 24X7 recording and monitoring.</p>
    <p class="tight">If you have any questions about us, our products or processes, please do not hesitate to call us.</p>
  </div>

  <div class="services">
    <h3>OUR SERVICES INCLUDE:</h3>
    <ul>
      <li>Installing Standalone DVR Sytem</li>
      <li>Installing PC based high quality DVR system</li>
      <li>Installing IP based megapixel CCTV System</li>
      <li>Services for home, office and business clients</li>
      <li>Complete CCTV package from 1 camera to multi sites system</li>
    </ul>
  </div>

  <div class="devices-photo" role="img" aria-label="Photo of a monitor, dome camera and three smartphones showing live camera views of a home"></div>
</section>

<section class="flyer flyer--back" aria-label="Flyer back">
  <div class="package package--1">
    <div class="package-photo" role="img" aria-label="Photo of an LCD monitor, DVR recorder and two dome cameras"></div>
    <h2 class="package-title">CCTV System Package 1</h2>
    <div class="package-sub">Standalone DVR System (2 Cameras)</div>
    <ul class="package-list">
      <li>2 X high resolution dome cameras</li>
      <li>1 X 4 channel standalone DVR</li>
      <li>500GB hard drive</li>
      <li>19" LCD monitor</li>
      <li>Remote access from PCs &amp; Phones*</li>
      <li>Easy to use</li>
      <li>1 Year Warranty</li>
      <li>Full system supplied &amp; installed</li>
    </ul>
    <div class="price">$1495 + GST*</div>
  </div>

  <div class="package package--2">
    <div class="package-photo" role="img" aria-label="Photo of an LCD monitor, DVR recorder and four dome cameras"></div>
    <h2 class="package-title">CCTV System Package 2</h2>
    <div class="package-sub">Standalone DVR System (4 Cameras)</div>
    <ul class="package-list">
      <li>4 X high resolution dome cameras</li>
      <li>1 X 4 channel standalone DVR</li>
      <li>500GB hard drive</li>
      <li>19" LCD monitor</li>
      <li>Remote access from PCs &amp; Phones*</li>
      <li>Easy to use</li>
      <li>1 Year Warranty</li>
      <li>Full system supplied &amp; installed</li>
    </ul>
    <div class="price">$2195 + GST*</div>
  </div>

  <div class="package package--3">
    <div class="package-photo" role="img" aria-label="Photo of an LCD monitor, DVR recorder and eight dome cameras"></div>
    <h2 class="package-title">CCTV System Package 3</h2>
    <div class="package-sub">Standalone DVR System (8 Cameras)</div>
    <ul class="package-list">
      <li>8 X high resolution dome cameras</li>
      <li>1 X 8 channel standalone DVR</li>
      <li>1 Terrabyte hard drive</li>
      <li>19" LCD monitor</li>
      <li>Remote access from PCs &amp; Phones*</li>
      <li>Easy to use</li>
      <li>1 Year Warranty</li>
      <li>Full system supplied &amp; installed</li>
    </ul>
    <div class="price">$3295 + GST*</div>
  </div>

  <div class="back-contact">14/6 Harlow Street, Merriden, NSW 2290 | <b>Phone:</b> 02 5550 1847 | <b>Email:</b> info@brightwardsecure.com.au</div>
  <div class="back-url">www.brightwardsecure.com.au</div>
</section>

</body>
</html>
```